Romantic Experiences Business Needs Banner Ad Design Project

We are going to run a branding campaign and we need banner ad design for a company based in Mexico City called "CARENSOLTA".

We create romantic experiences or moments for couples celebrating special dates, for instance birthdays, wedding anniversaries and original ways to give an engagement ring. These experiences may have components like romantic dinner, chamber musicians, astronomer, concierges, fireworks, mansions, romantic tours on helicopter and yacht.

The final design should communicate our main task "romantic moment design" and brand attributes: sophisticated, elegant and romantic.

You can visit the webpage at: http://www.carensolta.com.mx

Target Market(s)

People from 25 to 50 years old who wants to celebrate wedding anniversary or give an engagement ring

Industry/Entity Type

Wedding

Requirements
Must have
• - Logo
- Banner sizes: 300x250, 728x90,160x600
Nice to have
• - Call to Action
- Theme: "Diseño Momentos Románticos"

```html
<!DOCTYPE html>
<html lang="es">
<head>
<meta charset="utf-8">
<title>CARENSOLTA – Banners</title>
<link rel="stylesheet" href="https://fonts.googleapis.com/css2?family=Tinos&family=Roboto+Condensed:wght@400&display=swap">
<style>
  :root {
    --stage: #5a3019;
    --paper: #ffffff;
    --ink-brand: #2a2a2a;
    --ink-light: #ffffff;
    --dark-top: #3a3a3a;
    --dark-bottom: #111111;
    --orange: #f08a1c;
    --orange-light: #fbb040;
    --orange-deep: #e06a0b;
    --photo-a: #c9b9a8;
    --photo-b: #7d8f5c;
    --photo-c: #e8ddd2;
  }
  * { box-sizing: border-box; margin: 0; padding: 0; }
  html, body { width: 1200px; height: 816px; overflow: hidden; background: var(--stage); }
  .canvas { position: relative; width: 1200px; height: 816px; }
  .banner { position: absolute; overflow: hidden; background: linear-gradient(var(--dark-top), var(--dark-bottom)); }
  .banner svg.art { position: absolute; inset: 0; }

  .brand {
    position: absolute; display: flex; align-items: center; justify-content: center; gap: 8px;
    font-family: "Roboto Condensed", sans-serif; font-weight: 400; color: var(--ink-brand);
    letter-spacing: 0.06em; line-height: 1;
  }
  .brand-dot { flex: none; border-radius: 50%; background: var(--orange); }

  .headline { position: absolute; font-family: "Tinos", serif; font-weight: 400; color: var(--ink-light); line-height: 1.15; }
  .cta {
    position: absolute; display: flex; align-items: center; justify-content: space-between;
    padding: 0 8px 0 12px; border-radius: 4px;
    background: linear-gradient(var(--orange-light), var(--orange) 55%, var(--orange-deep));
    font-family: "Roboto Condensed", sans-serif; color: #2b1a08;
  }
  .cta svg { flex: none; }

  /* 160x600 */
  .sky { left: 21px; top: 21px; width: 196px; height: 731px; }
  .sky .brand { left: 0; top: 0; width: 100%; height: 60px; font-size: 24px; }
  .sky .brand-dot { width: 10px; height: 10px; }
  .sky .headline { left: 10px; top: 508px; width: 180px; }
  .sky .h-lg { display: block; font-size: 52px; line-height: 1.1; }
  .sky .h-md { display: block; font-size: 31px; }
  .sky .cta { left: 10px; top: 676px; width: 173px; height: 40px; font-size: 25px; }

  /* 300x250 */
  .square { left: 239px; top: 276px; width: 410px; height: 340px; }
  .square .brand { left: 0; top: 0; width: 100%; height: 72px; font-size: 40px; gap: 12px; }
  .square .brand-dot { width: 14px; height: 14px; }
  .square .headline { left: 0; top: 300px; width: 100%; text-align: center; font-size: 29px; }
  .square .cta { left: 118px; top: 256px; width: 173px; height: 37px; font-size: 25px; }

  /* 728x90 */
  .leader { left: 239px; top: 643px; width: 887px; height: 110px; }
  .leader .headline { left: 320px; top: 6px; }
  .leader .h-md { display: block; font-size: 34px; }
  .leader .h-lg { display: block; font-size: 52px; line-height: 1; }
  .leader .brand { left: 648px; top: 16px; width: 226px; height: 30px; font-size: 26px; color: var(--ink-light); }
  .leader .brand-dot { width: 9px; height: 9px; }
  .leader .cta { left: 680px; top: 60px; width: 163px; height: 36px; font-size: 23px; }
</style>
</head>
<body>
<main class="canvas">

  <section class="banner sky" aria-label="Banner 160x600">
    <svg class="art" width="196" height="731" viewBox="0 0 196 731">
      <defs>
        <linearGradient id="sky-photo" x1="0" y1="0" x2="1" y2="1">
          <stop offset="0" stop-color="var(--photo-c)"/>
          <stop offset="0.6" stop-color="var(--photo-a)"/>
          <stop offset="1" stop-color="#a89486"/>
        </linearGradient>
      </defs>
      <rect width="196" height="60" fill="var(--paper)"/>
      <path d="M0 60 H196 V440 Q100 452 0 445 Z" fill="url(#sky-photo)" role="img" aria-label="Fotografía de una pareja abrazada y sonriendo"/>
      <path d="M0 445 Q100 452 196 440 V452 Q100 462 0 458 Z" fill="var(--orange)"/>
    </svg>
    <div class="brand"><span class="brand-dot"></span><span>CARENSOLTA</span></div>
    <h2 class="headline"><span class="h-lg">Diseño</span><span class="h-md">Momentos</span><span class="h-md">Románticos</span></h2>
    <a class="cta"><span>CRÉALO</span>
      <svg width="24" height="24" viewBox="0 0 24 24"><circle cx="12" cy="12" r="11" fill="var(--orange-light)"/><path d="M6 12h9M12 8l4 4-4 4" stroke="#fff" stroke-width="2.4" fill="none"/></svg>
    </a>
  </section>

  <section class="banner square" aria-label="Banner 300x250">
    <svg class="art" width="410" height="340" viewBox="0 0 410 340">
      <defs>
        <linearGradient id="sq-photo" x1="0" y1="0" x2="1" y2="0">
          <stop offset="0" stop-color="var(--photo-b)"/>
          <stop offset="0.45" stop-color="var(--photo-c)"/>
          <stop offset="1" stop-color="var(--photo-a)"/>
        </linearGradient>
      </defs>
      <rect width="410" height="72" fill="var(--paper)"/>
      <path d="M0 72 H410 V246 Q260 268 0 272 Z" fill="url(#sq-photo)" role="img" aria-label="Fotografía de una pareja abrazada al aire libre"/>
      <path d="M0 272 Q260 268 410 246 V258 Q260 280 0 284 Z" fill="var(--orange)"/>
    </svg>
    <div class="brand"><span class="brand-dot"></span><span>CARENSOLTA</span></div>
    <a class="cta"><span>CRÉALO</span>
      <svg width="24" height="24" viewBox="0 0 24 24"><circle cx="12" cy="12" r="11" fill="var(--orange-light)"/><path d="M6 12h9M12 8l4 4-4 4" stroke="#fff" stroke-width="2.4" fill="none"/></svg>
    </a>
    <h2 class="headline">Diseño Momentos Románticos</h2>
  </section>

  <section class="banner leader" aria-label="Banner 728x90">
    <svg class="art" width="887" height="110" viewBox="0 0 887 110">
      <defs>
        <linearGradient id="ld-photo" x1="0" y1="0" x2="1" y2="0">
          <stop offset="0" stop-color="var(--photo-b)"/>
          <stop offset="0.4" stop-color="var(--photo-c)"/>
          <stop offset="1" stop-color="var(--photo-a)"/>
        </linearGradient>
      </defs>
      <path d="M0 0 H240 Q275 50 285 110 H0 Z" fill="url(#ld-photo)" role="img" aria-label="Fotografía de una pareja abrazada y sonriendo"/>
      <path d="M240 0 H252 Q290 50 300 110 H285 Q275 50 240 0 Z" fill="var(--orange)"/>
    </svg>
    <h2 class="headline"><span class="h-md">Diseño Momentos</span><span class="h-lg">Románticos</span></h2>
    <div class="brand"><span class="brand-dot"></span><span>CARENSOLTA</span></div>
    <a class="cta"><span>CRÉALO</span>
      <svg width="22" height="22" viewBox="0 0 24 24"><circle cx="12" cy="12" r="11" fill="var(--orange-light)"/><path d="M6 12h9M12 8l4 4-4 4" stroke="#fff" stroke-width="2.4" fill="none"/></svg>
    </a>
  </section>

</main>
</body>
</html>
```